Design for web based travel expence program

We need a design template for a web based travel expence program we have created. The current design is based on a standard framework, and it needs to be "spiced" up.
Please notice that there are only 3-4 screen shots that needs an "upspice" of the design. No complete web design is expected for this price. For the right designer we have many more jobs coming up!
Tovalin Accounting is a Scandinavian accounting company with offices in Norway (Oslo) and Stockholm (Sweden). Our goal is to be a proactive accounting company known for trouble-free solutions and wide knowledge about what we do. We have created an "easy" accounting program enabling clients to take picture of vouchers, upload them to our portal and gather them to a travel expense scheme that can be approved and sent directly into an accounting program.
The program is pure web based and created with sophisticated programming code, but only with a standard framework as design template. We need a touch of professional design that easily can be implemented “on top” of the framework.
We are thinking that the designer should add icons and create the squared elements a bit rounder and with a more beautiful touch.
We are looking for a designer that preferably can create CSS files with an improved design, though the first step should be to create some pictures/Photshop examples on how it could look like. The files we have uploaded are the screen shots that needs to be improved with a better design.
Reason: Thank you for the designs, but still a bit few to choose between.
Target Market(s)
All type of businesses, but the end user is in focus. The program is designed to be easy-to-learn and very useful for all persons dealing with travel expence forms.
Industry/Entity Type
Accounting

```html
<!DOCTYPE html>
<html lang="no">
<head>
<meta charset="utf-8">
<title>Refusjoner – Tovalin Accounting</title>
<link href="https://fonts.googleapis.com/css2?family=Lato:wght@400;700&display=swap" rel="stylesheet">
<style>
  :root {
    --bg-deep: #0a78c0;
    --bg-light: #5fb7d6;
    --bg-teal: #63aebf;
    --sidebar-top: #0b62b2;
    --sidebar-bottom: #0a4f9e;
    --nav-icon: #0c3f7c;
    --accent: #38a6dc;
    --accent-line: #6cc0e8;
    --header-top: #3a98d8;
    --header-bottom: #2f7dc4;
    --panel: #ffffff;
    --row-alt: #ebebeb;
    --row-line: #d6d6d6;
    --text: #555555;
    --white: #ffffff;
    --field-border: #d9d9d9;
  }
  * { box-sizing: border-box; margin: 0; padding: 0; }
  html, body { width: 1200px; height: 581px; overflow: hidden; }
  body {
    position: relative;
    font-family: "Lato", Arial, sans-serif;
    color: var(--text);
    background:
      radial-gradient(ellipse 420px 260px at 450px 440px, rgba(120,190,190,.55), transparent 70%),
      radial-gradient(ellipse 500px 320px at 700px 300px, rgba(110,195,230,.6), transparent 70%),
      linear-gradient(100deg, #4aa6d3 0%, var(--bg-light) 30%, var(--bg-teal) 50%, #2e9ad0 75%, var(--bg-deep) 100%);
  }

  .sidebar {
    position: absolute; left: 13px; top: 13px; width: 134px; height: 555px;
    border-radius: 3px;
    background: linear-gradient(180deg, var(--sidebar-top), var(--sidebar-bottom));
  }
  .nav-item {
    position: absolute; left: 11px; display: flex; align-items: center;
    color: var(--white); font-size: 9px; letter-spacing: .2px;
  }
  .nav-item--refunds { top: 25px; }
  .nav-item--receipts { top: 76px; }
  .nav-icon {
    width: 29px; height: 29px; border-radius: 50%; background: var(--nav-icon);
    display: flex; align-items: center; justify-content: center; margin-right: 7px;
  }
  .nav-divider {
    position: absolute; left: 11px; top: 63px; width: 113px; height: 1px;
    background: rgba(255,255,255,.18);
  }
  .nav-badge {
    display: inline-block; margin-left: 5px; padding: 0 3px; line-height: 10px;
    font-size: 8px; background: var(--accent); border-radius: 2px;
  }

  .panel {
    position: absolute; left: 160px; top: 13px; width: 1013px; height: 380px;
    background: var(--panel); border-radius: 3px;
  }
  .new-refund {
    position: absolute; left: 14px; top: 16px; width: 146px; height: 35px;
    background: var(--accent); border-radius: 2px; color: var(--white);
    font-size: 10px; display: flex; align-items: center; justify-content: space-between;
    padding: 0 10px 0 15px;
  }
  .search {
    position: absolute; left: 170px; top: 16px; width: 209px; height: 35px;
    border: 1px solid var(--field-border); border-radius: 3px;
    font-size: 10px; color: #444; display: flex; align-items: center;
    justify-content: space-between; padding: 0 8px 0 13px;
  }

  .filters {
    position: absolute; left: 14px; top: 61px; width: 146px; height: 293px;
    background: var(--accent); border-radius: 2px; padding: 4px 14px 0 16px;
    list-style: none;
  }
  .filters li {
    display: flex; justify-content: space-between; height: 38px; align-items: center;
    color: var(--white); font-size: 10px; border-bottom: 1px solid var(--accent-line);
  }
  .filters li:last-child { border-bottom: none; }

  .refund-table {
    position: absolute; left: 171px; top: 61px; width: 824px;
    border-collapse: collapse; font-size: 10px;
  }
  .refund-table th {
    height: 35px; text-align: left; font-weight: 400; font-size: 11px; color: var(--white);
    background: linear-gradient(180deg, var(--header-top), var(--header-bottom));
  }
  .refund-table th:first-child { border-radius: 3px 0 0 3px; }
  .refund-table th:last-child { border-radius: 0 3px 3px 0; }
  .refund-table td { height: 38px; border-bottom: 1px solid var(--row-line); }
  .refund-table tbody tr:nth-child(even) td { background: var(--row-alt); }
  .col-status { padding-left: 38px; width: 197px; }
  .col-title { width: 136px; }
  .col-receipts { width: 159px; }

  .footer-note {
    position: absolute; right: 27px; top: 556px; font-size: 8px; color: var(--white);
  }
</style>
</head>
<body>
  <nav class="sidebar">
    <div class="nav-item nav-item--refunds">
      <span class="nav-icon">
        <svg width="16" height="16" viewBox="0 0 16 16" fill="#fff">
          <circle cx="8" cy="3.5" r="2.3"/>
          <path d="M3 9h7.5a2 2 0 0 1 0 4H6v-1.5h4.5a.5.5 0 0 0 0-1H3z"/>
          <rect x="2" y="13.5" width="12" height="1.5" rx=".6"/>
        </svg>
      </span>
      REFUSJONER
    </div>
    <div class="nav-divider"></div>
    <div class="nav-item nav-item--receipts">
      <span class="nav-icon">
        <svg width="16" height="16" viewBox="0 0 16 16" fill="none" stroke="#fff" stroke-width="1.3">
          <path d="M4 2h7l2 2v10H4z" transform="rotate(-12 8 8)"/>
          <path d="M6 6h5M6 8.5h5M6 11h3" transform="rotate(-12 8 8)"/>
        </svg>
      </span>
      KVITTERINGER <span class="nav-badge">3</span>
    </div>
  </nav>

  <main class="panel">
    <div class="new-refund">
      Ny Refusjon
      <svg width="18" height="16" viewBox="0 0 18 16" fill="none" stroke="#fff" stroke-width="1.3">
        <path d="M11 3H2v12h11V8"/>
        <path d="M15 1l2 2-8 8H7V9z"/>
      </svg>
    </div>
    <div class="search">
      Sok
      <svg width="13" height="13" viewBox="0 0 13 13" fill="none" stroke="#c4c4c4" stroke-width="1.5">
        <circle cx="5" cy="5" r="3.8"/><path d="M8 8l4 4"/>
      </svg>
    </div>

    <ul class="filters">
      <li><span>Alle</span><span>[2]</span></li>
      <li><span>Lkke sendy</span><span>[2]</span></li>
      <li><span>Sendt</span><span>[0]</span></li>
      <li><span>Refundert</span><span>[0]</span></li>
    </ul>

    <table class="refund-table">
      <thead>
        <tr>
          <th class="col-status">Status</th>
          <th class="col-title">Tittel</th>
          <th class="col-receipts">Kvitteringer</th>
          <th>Belop</th>
        </tr>
      </thead>
      <tbody>
        <tr><td class="col-status">Ikke sendt</td><td>Reise</td><td>Ukraina</td><td>3&nbsp; 3910.54</td></tr>
        <tr><td class="col-status">Ikke sendt</td><td>Utlegg</td><td>Juni</td><td>0&nbsp; 0</td></tr>
        <tr><td class="col-status">Ikke sendt</td><td>Reise</td><td>Ukraina</td><td>3&nbsp; 3910.54</td></tr>
        <tr><td class="col-status">Ikke sendt</td><td>Utlegg</td><td>Juni</td><td>0&nbsp; 0</td></tr>
      </tbody>
    </table>
  </main>

  <p class="footer-note">Ver 0.1 © Tovalin Accounting.</p>
</body>
</html>
```